Business cards for KORU Real Estate Holdings LLC

We need a cool, original business card design for a company based in the Washington DC metropolitan area. We are a new energetic and passionate Real Estate Investing Company that invests in all types of real estate; commercial, residential, industrial etc.

Our company color is Red since it reflects action, energy and speed; it is assertive confident, energizing, exciting, powerful, passionate and determined. So we would like business card communicate those qualities to the audience.

Our audiences are investors that want to invest with us, real estate sellers, buyers, and tenants who lease from us.

Our logo is attached

```html
<!DOCTYPE html>
<html lang="en">
<head>
<meta charset="utf-8">
<title>KORU Real Estate Holdings LLC – Business Cards</title>
<link rel="stylesheet" href="https://fonts.googleapis.com/css2?family=Questrial&family=Open+Sans:wght@600&family=Cinzel:wght@400&display=swap">
<style>
  :root {
    --backdrop: #2b2b2d;
    --brand-red: #c61f26;
    --brand-red-deep: #a9171d;
    --card-white: #f4f4f4;
    --ink: #2a2a2a;
    --ink-soft: #3c3c3c;
    --paper-text: #ffffff;
  }
  * { margin: 0; padding: 0; box-sizing: border-box; }
  html, body {
    width: 1200px; height: 900px; overflow: hidden;
    background: var(--backdrop);
  }
  .canvas { position: relative; width: 1200px; height: 900px; }

  .card {
    position: absolute;
    width: 600px; height: 340px;
    box-shadow: 0 14px 30px rgba(0,0,0,0.45);
    overflow: hidden;
  }

  /* Back of card – red */
  .card--back {
    left: 110px; top: 110px;
    background: linear-gradient(160deg, var(--brand-red) 0%, var(--brand-red-deep) 100%);
  }
  .card--back .company-name {
    position: absolute; left: 0; right: 0; top: 112px;
    text-align: center;
    font-family: "Questrial", sans-serif;
    font-size: 30px; letter-spacing: 1px;
    color: var(--paper-text);
  }
  .card--back .tagline {
    position: absolute; left: 40px; bottom: 34px;
    font-family: "Open Sans", sans-serif; font-weight: 600;
    font-size: 15px; letter-spacing: 1.6px;
    color: var(--paper-text);
  }

  /* Front of card – white */
  .card--front {
    left: 490px; top: 450px;
    background: linear-gradient(160deg, #ffffff 0%, var(--card-white) 60%, #e6e6e6 100%);
  }
  .card--front .company-name {
    position: absolute; left: 0; right: 0; top: 52px;
    text-align: center;
    font-family: "Questrial", sans-serif;
    font-size: 28px; letter-spacing: 1px;
    color: var(--ink);
  }
  .person {
    position: absolute; right: 34px; top: 110px; text-align: right;
  }
  .person__name {
    font-family: "Cinzel", serif; font-size: 22px; color: var(--brand-red);
    letter-spacing: 0.5px;
  }
  .person__role {
    font-family: "Cinzel", serif; font-size: 15px; color: var(--ink-soft);
    letter-spacing: 0.5px;
  }

  .icon-rail {
    position: absolute; left: 0; top: 150px;
    width: 44px; height: 176px;
    background: var(--brand-red);
    border-radius: 0 10px 10px 0;
    display: flex; flex-direction: column; justify-content: space-around; align-items: center;
    padding: 8px 0;
  }
  .icon-rail svg { width: 20px; height: 20px; display: block; }

  .contact-list {
    position: absolute; left: 68px; top: 156px;
    list-style: none;
    font-family: "Questrial", sans-serif; font-size: 17px; color: var(--ink);
    line-height: 1.25;
  }
  .contact-list li { margin-bottom: 12px; }

  .base-band {
    position: absolute; left: 0; bottom: 0; width: 600px; height: 40px;
  }
</style>
</head>
<body>
<main class="canvas">

  <section class="card card--back" aria-label="Business card back">
    <p class="company-name">KORU Real Estate Holdings LLC</p>
    <p class="tagline">REAL ESTATE, COMMERCIAL, RESIDENTIAL, INDUSTRIAL</p>
  </section>

  <section class="card card--front" aria-label="Business card front">
    <p class="company-name">KORU Real Estate Holdings LLC</p>

    <div class="person">
      <p class="person__name">YOUR NAME</p>
      <p class="person__role">Designation</p>
    </div>

    <div class="icon-rail">
      <svg viewBox="0 0 24 24" aria-label="Phone"><path fill="#fff" d="M6.6 10.8a15 15 0 0 0 6.6 6.6l2.2-2.2c.3-.3.7-.4 1-.2 1.1.4 2.3.6 3.6.6.6 0 1 .4 1 1V20c0 .6-.4 1-1 1A17 17 0 0 1 3 4c0-.6.4-1 1-1h3.5c.6 0 1 .4 1 1 0 1.3.2 2.5.6 3.6.1.3 0 .7-.2 1z"/></svg>
      <svg viewBox="0 0 24 24" aria-label="Fax"><path fill="#fff" d="M7 3h10v5H7zM4 9h16a1 1 0 0 1 1 1v8h-4v3H7v-3H3v-8a1 1 0 0 1 1-1zm5 7v3h6v-3z"/></svg>
      <svg viewBox="0 0 24 24" aria-label="Email"><path fill="#fff" d="M3 5h18v14H3zm2 2v.4l7 5 7-5V7l-7 5z"/></svg>
      <svg viewBox="0 0 24 24" aria-label="Address"><path fill="#fff" d="M12 2a7 7 0 0 0-7 7c0 5 7 13 7 13s7-8 7-13a7 7 0 0 0-7-7zm0 9.5A2.5 2.5 0 1 1 12 6.5a2.5 2.5 0 0 1 0 5z"/></svg>
    </div>

    <ul class="contact-list">
      <li>07 41302256</li>
      <li>07 41302257</li>
      <li>Info@koru-holdings.com</li>
      <li>Your Complete<br>Address Details Here</li>
    </ul>

    <svg class="base-band" viewBox="0 0 600 40" preserveAspectRatio="none" aria-hidden="true">
      <path d="M0 30 L470 24 L600 22 L600 40 L0 40 Z" fill="#c61f26"/>
      <path d="M450 40 C470 40 470 8 500 6 L600 4 L600 40 Z" fill="#1c1c1c"/>
    </svg>
  </section>

</main>
</body>
</html>
```